2 Pager Flyer for Cyber Security Services

We need a company (B2B) professional flyer for our company services ). Text is attached (text is not final, but like this you have an idea of most important parts). To get an idea of our current website design, please visit https://brovel.com/html/tilmo/, but feel free to use your own images/style.

```html
<!DOCTYPE html>
<html lang="en">
<head>
<meta charset="utf-8">
<title>Tilmo – Two Page Flyer</title>
<link rel="stylesheet" href="https://fonts.googleapis.com/css2?family=Poppins:wght@300;400;500;600;700;800&family=Roboto+Condensed:wght@400;500&family=Oswald:wght@400;500&display=swap">
<style>
:root{
  --bg:#e9e9ec;
  --ink:#1b1d22;
  --dark:#2a2d35;
  --night:#0f1218;
  --night-2:#1f2531;
  --blue:#1f8ed6;
  --blue-light:#e3eef8;
  --white:#ffffff;
  --grey:#9aa3b0;
  --muted:#4b5160;
}
*{box-sizing:border-box;margin:0;padding:0}
html,body{width:939px;height:1200px;overflow:hidden}
body{background:var(--bg);position:relative;font-family:"Roboto Condensed",sans-serif;color:var(--ink)}
.page{position:absolute;top:302px;width:460px;height:596px;overflow:hidden}

/* ---------- Page 1 : risks ---------- */
.risks{left:2px;background:var(--white)}
.risks__header{position:absolute;left:0;top:0;width:460px;height:46px}
.risks__band{position:absolute;left:0;top:0}
.brand-name{font-family:"Poppins",sans-serif;font-weight:300;letter-spacing:1px}
.risks__logo{position:absolute;left:11px;top:6px;font-size:27px;color:var(--ink)}
.risks__title{position:absolute;left:133px;top:14px;font-family:"Poppins",sans-serif;font-weight:700;font-size:12.4px;color:var(--white)}
.risk-list{position:absolute;left:0;top:68px;width:460px;list-style:none}
.risk{padding:3px 20px 4px 20px;position:relative}
.risk:nth-child(even){background:var(--blue-light)}
.risk::before{content:"";position:absolute;left:9px;top:5px;width:6px;height:6px;border-radius:50%;background:var(--dark)}
.risk__title{font-family:"Oswald",sans-serif;font-weight:400;font-size:7px;color:var(--blue);text-transform:uppercase;letter-spacing:.1px;line-height:10px}
.risk__text{font-size:6.1px;line-height:10px;color:var(--ink);text-align:justify}
.cases{position:absolute;left:19px;top:446px;display:flex;gap:5px}
.case{width:98px}
.case__photo{width:98px;height:67px;background:linear-gradient(135deg,#5b6472,#1b2a3c)}
.case:nth-child(2) .case__photo{background:linear-gradient(135deg,#0c1a2a,#1d5a80)}
.case:nth-child(3) .case__photo{background:linear-gradient(135deg,#2f6ea1,#c9d9ea)}
.case__caption{font-family:"Poppins",sans-serif;font-weight:600;font-size:5.6px;line-height:8px;text-align:center;margin-top:11px}
.illustration{position:absolute;left:343px;top:409px;width:117px;height:136px;border-radius:40px 0 0 0;background:linear-gradient(160deg,#d6d8dc,#8e9299)}
.risks__footer{position:absolute;left:0;bottom:0;width:460px;height:39px}
.contact{position:absolute;top:0;height:39px;display:flex;align-items:center;gap:6px;font-family:"Poppins",sans-serif;font-weight:300;font-size:9.4px;color:var(--white)}
.contact svg{width:14px;height:14px}

/* ---------- Page 2 : monitoring ---------- */
.monitor{left:477px;background:linear-gradient(180deg,var(--night) 0%,#141821 45%,var(--night-2) 100%);color:var(--white)}
.monitor__texture{position:absolute;left:135px;top:0;width:180px;height:60px;background:radial-gradient(ellipse at 50% 30%,rgba(150,155,165,.45),rgba(150,155,165,0) 70%)}
.monitor__logo{position:absolute;left:0;right:0;top:52px;text-align:center;font-size:43px;color:var(--white);line-height:44px}
.monitor__headline{position:absolute;left:0;right:0;top:136px;text-align:center;font-family:"Poppins",sans-serif;font-weight:700;font-size:16.6px}
.monitor__question{position:absolute;left:0;right:0;top:172px;text-align:center;font-family:"Poppins",sans-serif;font-weight:800;font-size:16.6px;color:var(--blue)}
.monitor__intro{position:absolute;left:10px;right:10px;top:199px;text-align:center;font-family:"Poppins",sans-serif;font-weight:600;font-size:7px;line-height:12.2px}
.exposures{position:absolute;left:38px;top:252px;display:flex;gap:7px}
.exposure{width:124px;height:52px;border:1.6px solid var(--blue);border-radius:6px;text-align:center;font-family:"Poppins",sans-serif;font-weight:300;font-size:6.8px;line-height:14.5px;padding-top:10px}
.msp__title{position:absolute;left:0;right:0;top:351px;text-align:center;font-family:"Oswald",sans-serif;font-weight:400;font-size:15px;color:var(--blue);letter-spacing:.2px}
.msp-list{position:absolute;left:11px;right:10px;top:375px;list-style:none}
.msp-list li{position:relative;padding-left:8px;font-size:5.3px;line-height:8px;margin-bottom:7.6px}
.msp-list li::before{content:"";position:absolute;left:0;top:1.5px;border-left:4px solid var(--blue);border-top:3px solid transparent;border-bottom:3px solid transparent}
.steps{position:absolute;left:12px;right:40px;top:509px;list-style:none}
.step{position:relative;padding-left:10px;margin-bottom:7px;font-family:"Poppins",sans-serif;font-size:4.6px;line-height:6.6px}
.step::before{content:"";position:absolute;left:0;top:1px;width:5px;height:17px;background:var(--blue)}
.step__title{font-weight:500;color:var(--white)}
.step__text{font-weight:300;color:var(--grey)}
</style>
</head>
<body>

<section class="page risks">
  <header class="risks__header">
    <svg class="risks__band" width="460" height="46" viewBox="0 0 460 46">
      <polygon points="122,0 460,0 460,46 100,46" fill="var(--dark)"/>
      <polygon points="122,0 135,0 113,46 100,46" fill="#3d424d"/>
    </svg>
    <div class="risks__logo brand-name">TILMO</div>
    <h1 class="risks__title">What Risks Can Be Mitigated With Tilmo?</h1>
  </header>

  <ul class="risk-list">
    <li class="risk">
      <h2 class="risk__title">Prevent phishing</h2>
      <p class="risk__text">We monitor all new domain registrations (ccTLDs, gTLDs, uTLD, sTLD). In doing so, we also record typical typosquatting techniques. Tilmo automatically analyzes domains that appear suspicious, capturing key properties such as WHOIS, geolocation, open web services, screenshots, similarity to the original site (AI analysis) etc. With our certificate log monitoring service you will also detect scammers using the same name on a SSL certificate as your protected asset.</p>
    </li>
    <li class="risk">
      <h2 class="risk__title">Detect exposed infrastructure</h2>
      <p class="risk__text">We monitor server access, IOT (Scanly) or complete DB dumps in different formats (CSV, Memory Dumps, Office Files etc). We regularly also examine also object storage buckets for sensitive data. Tilmo also provides a search option to query regularly updated botnet logs for domain names, brands or IP addresses as malicious actors have built vast networks of hacked computers that can be rented or purchased and used for cyberattacks such as distributed denial of service, fraud, spam or phishing.</p>
    </li>
    <li class="risk">
      <h2 class="risk__title">Detect leaks from ransomware</h2>
      <p class="risk__text">In ransomware attacks, victims are blackmailed into paying a ransom sum in order to regain access to their own data. In some cases, ransoms are not paid or, despite payment of ransom, the stolen data is uploaded to the Internet or darknet for every user to see. We monitor common ransomware groups and can inform the customer if stolen data is shared with the public.</p>
    </li>
    <li class="risk">
      <h2 class="risk__title">Find exposed data in the darknet</h2>
      <p class="risk__text">Monitoring whether your organisation's name appears in Dark Web forums, Onion-, I2P and paste sites can help you detect potential insider threats, enabling you to prevent data leaks and other incidents that may damage your organisation. Access to leacked accounts and passwords is also a popular darknet commodity. Passwords are valuable because attackers know that people tend to reuse their passwords for multiple accounts.</p>
    </li>
    <li class="risk">
      <h2 class="risk__title">Detect spoofing and impersonation</h2>
      <p class="risk__text">We monitor social media services such as Chirpy, Threadly, Vidstream, Pingram, etc. for posts that could be damaging to our reputation. We also detect attempts to create fake user profiles of key executives. Especially in the case of phishing and spoofing attacks, in which a false identity is simulated, such attacks should already be detected in the preparation phase.</p>
    </li>
    <li class="risk">
      <h2 class="risk__title">Understand employee exposure</h2>
      <p class="risk__text">Employees who are heavily exposed to the Internet are at greater risk of social engineering attacks such as phishing. Therefore, in Tilmo we measure how exposed an employee is on the Internet and where indications of activities related to the specific email account can be found.</p>
    </li>
    <li class="risk">
      <h2 class="risk__title">Detect stolen data</h2>
      <p class="risk__text">In Tilmo we offer the possibility to monitor credit card information (name, part of number etc) on the darknet. If such data is offered for sale in relevant forums as part of a phishing or malware attack, we can inform the owner promptly.</p>
    </li>
    <li class="risk">
      <h2 class="risk__title">And many more risk indicators</h2>
      <p class="risk__text">Tilmo is constantly under development and we see ourselves as a one-stop-shop for various cyber threat intelligence indicators. We will be happy to show you a detailed list of all the data sources we monitor and are still developing in a personal meeting.</p>
    </li>
  </ul>

  <div class="cases">
    <figure class="case">
      <div class="case__photo" role="img" aria-label="Photo of rows of security cameras"></div>
      <figcaption class="case__caption">Norvane experinced a<br>cyber attack</figcaption>
    </figure>
    <figure class="case">
      <div class="case__photo" role="img" aria-label="Photo of a hooded hacker at a desk in a dark room"></div>
      <figcaption class="case__caption">Z9x Ransomware back<br>online, 21 victims in a month</figcaption>
    </figure>
    <figure class="case">
      <div class="case__photo" role="img" aria-label="Photo of hands typing on a keyboard with a lock overlay"></div>
      <figcaption class="case__caption">Bq7 banking solution<br>hacked, data leaked online</figcaption>
    </figure>
  </div>
  <div class="illustration" role="img" aria-label="Greyscale illustration of a hacker at a computer with security icons"></div>

  <footer class="risks__footer">
    <svg width="460" height="39" viewBox="0 0 460 39" style="position:absolute;left:0;top:0">
      <rect width="460" height="39" fill="var(--dark)"/>
      <polygon points="318,0 460,0 460,39 300,39" fill="var(--blue)"/>
    </svg>
    <div class="contact" style="left:20px">
      <svg viewBox="0 0 14 14"><circle cx="7" cy="7" r="6.2" fill="none" stroke="#fff" stroke-width="1"/><path d="M4.6 3.8l1.3 1.4-.6.9c.5 1 1.3 1.8 2.3 2.3l.9-.6 1.4 1.3-.8 1.1C6.8 10 4 7.2 3.6 4.6z" fill="#fff"/></svg>
      +41 79 4402188
    </div>
    <div class="contact" style="left:132px">
      <svg viewBox="0 0 14 14"><circle cx="7" cy="7" r="6.2" fill="none" stroke="#fff" stroke-width="1"/><rect x="3.8" y="4.8" width="6.4" height="4.4" fill="none" stroke="#fff" stroke-width=".8"/><path d="M3.8 4.8L7 7.4l3.2-2.6" fill="none" stroke="#fff" stroke-width=".8"/></svg>
      switzerland@tilmo.io
    </div>
    <div class="contact" style="left:327px">
      <svg viewBox="0 0 14 14"><circle cx="7" cy="7" r="6.2" fill="none" stroke="#fff" stroke-width="1"/><circle cx="7" cy="7" r="3.6" fill="none" stroke="#fff" stroke-width=".7"/><ellipse cx="7" cy="7" rx="1.6" ry="3.6" fill="none" stroke="#fff" stroke-width=".7"/><path d="M3.4 7h7.2" stroke="#fff" stroke-width=".7"/></svg>
      www.tilmo.io
    </div>
  </footer>
</section>

<section class="page monitor">
  <div class="monitor__texture" role="img" aria-label="Soft halftone dot decoration"></div>
  <div class="monitor__logo brand-name">TILMO</div>
  <h1 class="monitor__headline">Is Your Clients Data In The Dark Web?</h1>
  <h2 class="monitor__question">WHAT DO WE MONITOR IN TILMO?</h2>
  <p class="monitor__intro">Tilmo helps you understand when, where and how stolen or accidentally<br>leaked information in dark web markets, forums, botnet logs, IRC, social media and other sources is exposed.<br>Setup in minutes you will receive instant access to real-time reporting including:</p>

  <div class="exposures">
    <div class="exposure">Infrastructure exposure:<br>IOT, Git, CloudHub, RepoVault &amp; more</div>
    <div class="exposure">People exposure:<br>Social media monitoring</div>
    <div class="exposure">Ransomware exposure:<br>leak &amp; credential monitoring</div>
  </div>

  <h2 class="msp__title">OPTIMIZED FOR MANAGED SERVICE PROVIDERS</h2>
  <ul class="msp-list">
    <li>No need for long commitments: Our SaaS platform can be booked as a one-time access to analyze the exposure in the darknet or as a permanent dark web monitoring tool, which alerts the customer immediately in case of a data leakage.</li>
    <li>Flexible clients data search: Use any search term in Tilmo provided by your clients without any complicated registration and validation process</li>
    <li>Flexible pricing: Fixed, very favorable prices that are not dependent on the size of the company mean higher margins, but also the possibility to serve markets that do not have access to it due to the usually elevated prices. We offer Pay-As-You-Go models or as an alternative we can create a package at a fixed price for one year in advance - with the according discounts. You have no risk: If the planned budget is not used up, the license can be transferred in the following year without additional costs.</li>
    <li>Quick Setup: No installation. No agents. Just Real-Time, Actionable Intel</li>
    <li>Know-how transfer: Not sure what to query and how to interpret the data? No worries! We assist you in the setup and analysis of the data. From security experts for security experts: Our experienced penetration testers and former hackers are at your disposal. Because you have better things to do than follow red herrings, go down rabbit holes and chase phantom threats.</li>
  </ul>

  <ol class="steps">
    <li class="step">
      <div class="step__title">Partner onboarding</div>
      <div class="step__text">After the free registration on Tilmo, we will give your team a short introduction to Tilmo and show<br>how to retrieve data from the different sources and filter it for relevant risks.</div>
    </li>
    <li class="step">
      <div class="step__title">Client Onboarding</div>
      <div class="step__text" style="color:var(--white)">For your first project, our team will again support you in creating the correct search queries and evaluations. If required,<br>you can also create your own accounts on Tilmo for your clients.</div>
    </li>
    <li class="step">
      <div class="step__title">Pay-as-you-go or fixed budget in advance</div>
      <div class="step__text">Payment can be made only after successful completion of the project: There are no financial risks for our partners due to high upfront investments.</div>
    </li>
  </ol>
</section>

</body>
</html>
```